Update Old OR create new Website

Current Website is looking a bit old, I did this one a few years back.

Would like a fresh new look, current website sitepress theme is " the Vanta theme" from plumcrate and I just purchased this theme - "bravlo" also from plumcrate, I quite like the look of - http://bravlo.quorvex-skins.com/tech-business/ and if we could get somthing simlar would be great.

current website is at http://www.hle.com.au, have been playing around with the slider that i like.

I have said 5 pages to be designed but really it is just a 5 page website where most pages will look the same.

Any questions please let me know

Target Market(s)

Business

Coding

Coded - Design and coding required

Number of Pages Required

5+ page

Font styles to use
Sans Serif

Colors
33a6d7
0292cd
ffffff
0255a3

Requirements
Must have
• Device compatibility - pc, tablet, phone
Nice to have
• video
Should not have
• vunerabilities. Must also use images that will expire or disappear, ie must be uploaded to site not links to elsewhere.

```html
<!DOCTYPE html>
<html lang="en">
<head>
<meta charset="utf-8">
<title>HLE Technologies – Home</title>
<link href="https://fonts.googleapis.com/css2?family=Poppins:wght@300;400;500&display=swap" rel="stylesheet">
<style>
:root{
  --stage:#13233f;
  --accent:#1aa7d8;
  --accent-dark:#0292cd;
  --ink:#1d1d1d;
  --muted:#8a8a8a;
  --pale:#eaf6fb;
  --grey:#e3e3e3;
  --bar:#0b0b0b;
  --hero-a:#1c3d6b;
  --hero-b:#24508a;
  --panel:rgba(38,38,38,.92);
}
*{box-sizing:border-box;margin:0;padding:0}
html,body{width:1200px;height:1200px;overflow:hidden}
body{background:var(--stage);font-family:"Poppins",sans-serif;color:var(--ink)}
.site{position:absolute;left:362px;top:38px;width:476px;height:1124px;background:#fff;overflow:hidden}
.abs{position:absolute}
.center{text-align:center;left:0;right:0}

.topbar{left:0;top:0;width:476px;height:12px;background:var(--bar);color:#ccc;font-size:3px;display:flex;align-items:center;padding:0 60px;justify-content:space-between}
.topbar .contact span{margin-right:6px}
.topbar .social{display:flex;gap:4px}
.topbar .social i{width:4px;height:4px;border-radius:50%;background:#ddd;display:block}

.header{left:0;top:12px;width:476px;height:26px;border-bottom:1px solid #eee;display:flex;align-items:center;padding:0 60px;justify-content:space-between}
.brand{display:flex;align-items:center;gap:3px;font-size:6px;font-weight:500;color:var(--ink)}
.brand .mark{width:6px;height:6px;background:var(--accent);border-radius:50%}
.brand small{font-size:3px;font-weight:400;margin-left:4px}
.nav{display:flex;gap:5px;font-size:3.4px;color:#333;align-items:center}
.nav .active{color:var(--accent)}
.nav .search{width:3.5px;height:3.5px;border:.6px solid #333;border-radius:50%}

.hero{left:0;top:38px;width:476px;height:186px;background:linear-gradient(135deg,var(--hero-a),var(--hero-b) 55%,var(--hero-a))}
.hero-title{top:99px;font-size:13px;font-weight:400;color:#fff;letter-spacing:.3px}
.hero-sub{top:118px;font-size:4.6px;color:#e6eef7;line-height:7px}
.hero-btns{top:152px;display:flex;justify-content:center;gap:6px}
.btn{height:13px;width:44px;border-radius:7px;font-size:6px;color:#fff;display:flex;align-items:center;justify-content:center}
.btn.primary{background:var(--accent-dark)}
.btn.dark{background:#172a44}
.dots{top:203px;display:flex;justify-content:center;gap:6px}
.dots i{width:5px;height:2px;background:#fff;display:block}
.dots i.on{background:var(--accent)}

h2{font-size:11px;font-weight:400;letter-spacing:.2px}
h2 b{color:var(--accent);font-weight:400;font-size:13px}
.lede{font-size:4.4px;color:var(--muted);line-height:7px}

.about-title{top:245px}
.about-lede{top:265px}
.about-copy{left:60px;top:310px;width:182px;font-size:4.5px;line-height:9.7px;color:#444}
.more{left:60px;top:345px;font-size:6px;color:var(--accent)}
.about-art{left:260px;top:302px;width:156px;height:78px;background:linear-gradient(180deg,#f5f7f9,#e4e9ee);border-radius:2px}

.services{left:0;top:410px;width:476px;height:202px;background:var(--pale)}
.services-title{top:443px}
.services-lede{top:460px}
.service{top:497px;width:80px;text-align:center}
.service .disc{width:42px;height:42px;border-radius:50%;background:var(--grey);margin:0 auto;display:flex;align-items:center;justify-content:center}
.service.active .disc{background:var(--accent)}
.service h3{font-size:6.4px;font-weight:400;margin-top:9px}
.service.active h3{color:var(--accent)}
.service p{font-size:3.8px;line-height:7.2px;color:var(--muted);margin-top:2px}

.quote{top:633px;font-size:7.8px;line-height:11px;color:#222}
.work{top:668px;width:84px;height:104px}
.work.feature{background:linear-gradient(160deg,#1b2433,#0d1320);color:#fff;padding:0 9px;display:flex;flex-direction:column;justify-content:center;text-align:center}
.work.feature h4{font-size:8px;font-weight:300;color:var(--accent)}
.work.feature p{font-size:3.6px;line-height:6px;margin-top:4px;color:#ddd}
.work.feature a{font-size:3.4px;color:var(--accent);margin-top:5px}
.ph-laptop{background:linear-gradient(150deg,#f1f2f4,#9aa2ad)}
.ph-phone{background:linear-gradient(150deg,#4a4a4a,#c9b6a3)}
.ph-devices{background:linear-gradient(150deg,#d9dde2,#6b7480)}
.arrow{width:15px;height:15px}

.testimonials{left:0;top:815px;width:476px;height:187px;background:linear-gradient(120deg,#3b3b3b,#232323 50%,#2f2f2f)}
.card{top:837px;width:104px;height:82px;background:var(--panel);padding:14px 14px 0 14px;color:#eee}
.card::after{content:"";position:absolute;left:14px;bottom:-5px;border-left:5px solid transparent;border-right:5px solid transparent;border-top:5px solid var(--panel)}
.card h4{font-size:6.2px;font-weight:400;color:var(--accent);margin-bottom:5px}
.card p{font-size:3.9px;line-height:7.3px}
.person{top:933px;display:flex;align-items:center;gap:9px}
.avatar{width:28px;height:28px;border-radius:50%;background:linear-gradient(160deg,#d7d7d7,#8d8d8d);border:1px solid #fff}
.person b{display:block;font-size:6.3px;font-weight:400;color:#fff}
.person span{display:block;font-size:4.4px;color:var(--accent)}

.footer h5{font-size:5.5px;font-weight:400;top:1038px}
.fcol{top:1053px;font-size:3.4px;color:var(--muted);line-height:6.4px}
.fcol .hi{color:var(--accent)}
.field{width:65px;height:9px;background:#d9d9d9;font-size:3px;color:#888;padding:3px 5px}
.send{width:22px;height:8px;background:var(--accent);font-size:3px;color:#fff;display:flex;align-items:center;justify-content:center}
.follow{top:1054px;display:flex;gap:3px}
.follow i{width:9px;height:9px;border:.6px solid #bbb;border-radius:50%;display:block}
.bottombar{left:0;top:1111px;width:476px;height:13px;background:var(--bar);color:#ccc;font-size:3.2px;display:flex;align-items:center;justify-content:center}
</style>
</head>
<body>
<div class="site">

  <div class="abs topbar">
    <div class="contact"><span>◦ 14 RIDGE ST, UPPER HOLLOW</span><span>◦ 1300 555 018</span><span>✉ INFO@HLE.COM.AU</span></div>
    <div class="social"><i></i><i></i><i></i><i></i></div>
  </div>

  <header class="abs header">
    <div class="brand"><span class="mark"></span>HLE Technologies<small>1300 555 018</small></div>
    <nav class="nav">
      <span class="active">HOME</span><span>SERVERS</span><span>NETWORKS</span><span>MANAGED IT</span><span>WEB</span><span>APPS</span><span>INTERNET</span><span>CONTACT</span><span class="search"></span>
    </nav>
  </header>

  <section class="abs hero" role="img" aria-label="Blue network of connected points and lines"></section>
  <h1 class="abs center hero-title">LOREM IPSUM</h1>
  <p class="abs center hero-sub">"Neque porro quisquam est qui dolorem ipsum quia dolor sit amet,<br>consectetur, adipisci velit..."</p>
  <div class="abs center hero-btns"><span class="btn primary">Try It</span><span class="btn dark">Login</span></div>
  <div class="abs center dots"><i></i><i class="on"></i><i></i></div>

  <h2 class="abs center about-title">ABOUT <b>US</b></h2>
  <p class="abs center lede about-lede">"Neque porro quisquam est qui dolorem ipsum quia dolor sit amet,<br>consectetur, adipisci velit..."</p>
  <p class="abs about-copy">It is a long established fact that a reader will be distracted by the read-able content of a page when looking at its layout. The point of using Lorem Ipsum is that it has a more-or-less normal distribution of letters, as opposed to using 'Content here, content here', making it look like read-able English.</p>
  <span class="abs more" style="top:404px">Read More ◦</span>
  <div class="abs about-art" role="img" aria-label="Desktop computer on a white desk with lamp and accessories"></div>

  <section class="abs services"></section>
  <h2 class="abs center services-title">WHAT WE <b>DO</b></h2>
  <p class="abs center lede services-lede">"Neque porro quisquam est qui dolorem ipsum quia dolor sit amet,<br>consectetur, adipisci velit..."</p>

  <div class="abs service active" style="left:53px">
    <div class="disc"><svg width="20" height="20" viewBox="0 0 24 24" fill="none" stroke="#fff" stroke-width="1.4"><rect x="3" y="4" width="18" height="12" rx="1"/><path d="M9 20h6M12 16v4"/></svg></div>
    <h3>Coding</h3><p>Lorem ipsum dolor sit amet,<br>consectetuer adipiscing elit, sed<br>diam nonummy nibh.</p>
  </div>
  <div class="abs service" style="left:146px">
    <div class="disc"><svg width="20" height="20" viewBox="0 0 24 24" fill="none" stroke="#333" stroke-width="1.2"><path d="M20 4 10 14M10 14l-2-2M8 12c-2 0-4 2-4 6 3 0 6-1 6-4"/></svg></div>
    <h3>Design</h3><p>Lorem ipsum dolor sit amet,<br>consectetuer adipiscing elit, sed<br>diam nonummy nibh.</p>
  </div>
  <div class="abs service" style="left:239px">
    <div class="disc"><svg width="20" height="20" viewBox="0 0 24 24" fill="none" stroke="#333" stroke-width="1.2"><circle cx="12" cy="12" r="2"/><circle cx="5" cy="5" r="1.5"/><circle cx="19" cy="5" r="1.5"/><circle cx="5" cy="19" r="1.5"/><circle cx="19" cy="19" r="1.5"/><path d="M6 6l4.5 4.5M18 6l-4.5 4.5M6 18l4.5-4.5M18 18l-4.5-4.5"/></svg></div>
    <h3>Networking</h3><p>Lorem ipsum dolor sit amet,<br>consectetuer adipiscing elit, sed<br>diam nonummy nibh.</p>
  </div>
  <div class="abs service" style="left:333px">
    <div class="disc"><svg width="20" height="20" viewBox="0 0 24 24" fill="none" stroke="#333" stroke-width="1.2"><circle cx="12" cy="12" r="3"/><path d="M12 3v3M12 18v3M3 12h3M18 12h3M5.6 5.6l2.1 2.1M16.3 16.3l2.1 2.1M5.6 18.4l2.1-2.1M16.3 7.7l2.1-2.1"/><circle cx="12" cy="12" r="6.5"/></svg></div>
    <h3>Testing</h3><p>Lorem ipsum dolor sit amet,<br>consectetuer adipiscing elit, sed<br>diam nonummy nibh.</p>
  </div>

  <p class="abs center quote">"Neque porro quisquam est qui dolorem ipsum quia dolor sit amet,<br>consectetur, adipisci velit..."</p>
  <div class="abs work feature" style="left:60px" role="img" aria-label="Dark screen with code behind the card text">
    <h4>SEO &amp; Analytics</h4>
    <p>It is a long established fact that a reader will be distracted by the readable content of a page when looking at its layout.</p>
    <a>Read More ›</a>
  </div>
  <div class="abs work ph-laptop" style="left:150px" role="img" aria-label="Laptop showing charts"></div>
  <div class="abs work ph-phone" style="left:241px" role="img" aria-label="Hand holding a smartphone with app icons"></div>
  <div class="abs work ph-devices" style="left:331px" role="img" aria-label="Website shown across desktop, tablet and phone"></div>
  <svg class="abs arrow" style="left:211px;top:791px" viewBox="0 0 16 16" fill="none" stroke="#333" stroke-width=".8"><circle cx="8" cy="8" r="7.3"/><path d="M10 5 6 8l4 3z"/></svg>
  <svg class="abs arrow" style="left:247px;top:791px" viewBox="0 0 16 16" fill="none" stroke="#333" stroke-width=".8"><circle cx="8" cy="8" r="7.3"/><path d="M6 5l4 3-4 3z"/></svg>

  <section class="abs testimonials" role="img" aria-label="Dim desk with keyboard, hands and wristwatch"></section>
  <div class="abs card" style="left:60px"><h4>Lorem Ipsum</h4><p>Contrary to popular belief, Lorem Ipsum is not simply random text. It has roots in a piece of classical Latin literature from 45 BC, making it over 2000 years old.</p></div>
  <div class="abs card" style="left:188px;top:839px"><h4>Lorem Ipsum</h4><p>Contrary to popular belief, Lorem Ipsum is not simply random text. It has roots in a piece of classical Latin literature from 45 BC, making it over 2000 years old.</p></div>
  <div class="abs card" style="left:314px"><h4>Lorem Ipsum</h4><p>Contrary to popular belief, Lorem Ipsum is not simply random text. It has roots in a piece of classical Latin literature from 45 BC, making it over 2000 years old.</p></div>
  <div class="abs person" style="left:60px"><div class="avatar" role="img" aria-label="Portrait of Owen Harlow"></div><div><b>Owen Harlow</b><span>Manager</span></div></div>
  <div class="abs person" style="left:186px"><div class="avatar" role="img" aria-label="Portrait of Lukas Brenner"></div><div><b>Lukas Brenner</b><span>CEO</span></div></div>
  <div class="abs person" style="left:314px"><div class="avatar" role="img" aria-label="Portrait of Marco Delane"></div><div><b>Marco Delane</b><span>Co. Manager</span></div></div>
  <svg class="abs arrow" style="left:211px;top:982px" viewBox="0 0 16 16" fill="none" stroke="#fff" stroke-width=".8"><circle cx="8" cy="8" r="7.3"/><path d="M10 5 6 8l4 3z"/></svg>
  <svg class="abs arrow" style="left:247px;top:982px" viewBox="0 0 16 16" fill="none" stroke="#fff" stroke-width=".8"><circle cx="8" cy="8" r="7.3"/><path d="M6 5l4 3-4 3z"/></svg>

  <footer class="footer">
    <h5 class="abs" style="left:60px">CONTACT US</h5>
    <div class="abs fcol" style="left:60px;width:78px">◦ Lorem Ipsum is simply dummy text of the typesetting industry<br><br>✆ (123) 456-7890<br>✉ info@hlemail.com</div>
    <h5 class="abs" style="left:165px">MENU</h5>
    <div class="abs fcol" style="left:165px">› <span class="hi">HOME</span><br>› SERVERS<br>› NETWORKS<br>› MANAGED IT</div>
    <div class="abs fcol" style="left:203px">› WEB<br>› APPS<br>› INTERNET<br>› CONTACT</div>
    <h5 class="abs" style="left:266px">NEWSLETTER</h5>
    <div class="abs field" style="left:266px;top:1051px">Name</div>
    <div class="abs field" style="left:266px;top:1064px">Email</div>
    <div class="abs send" style="left:266px;top:1078px">Send</div>
    <h5 class="abs" style="left:374px">FOLLOW US:</h5>
    <div class="abs follow" style="left:374px"><i></i><i></i><i></i><i></i></div>
  </footer>
  <div class="abs bottombar">All Rights Reserved Terms of Use and Privacy Policy</div>
</div>
</body>
</html>
```